Eye catching and professional flyer

We would like a flyer done for promo, predominately attached to emails and printed to advertise our business. We provide employment advice to Employers so its pretty straight forward. Shouldn't need lots of words. Needs to be catchy, exude confidence and look slick and professional.

Attached is our logo, some general info you may choose to use and some headlines. These are real headlines that we thought might be cool to be presented somehow as a hook and a fear motivator.
Updates

Project Deadline Extended Reason: I need the headlines to be displayed as though in newspaper. EG $5 squabble etc . Added Thursday, June 15, 2017

Target Market(s)

Employers in SME Companies

Industry/Entity Type

Business

Font styles to use
Serif
Sans Serif

Colors

Designer to choose colors to be used in the design.

Requirements
Must have
• Eye catching, professional. Imagery and pop out wording. Not lots and lots of text.
Should not have
• Be boring and amateur.

```html
<!DOCTYPE html>
<html lang="en">
<head>
<meta charset="utf-8">
<title>StaffSense Flyer</title>
<link href="https://fonts.googleapis.com/css2?family=Raleway:wght@400;500;600;700&family=Oswald:wght@300;600&display=swap" rel="stylesheet">
<style>
  :root{
    --orange:#f15a29;
    --slate:#464e5d;
    --ink:#3c4250;
    --ink-soft:#555b66;
    --paper:#ffffff;
    --stage:#2b2b2b;
    --rule:#d6d8dc;
  }
  *{box-sizing:border-box;margin:0;padding:0}
  html,body{width:1200px;height:1200px;overflow:hidden;background:var(--stage)}
  .canvas{position:relative;width:1200px;height:1200px}
  .flyer{
    position:absolute;left:180px;top:6px;width:895px;height:1265px;
    transform:scale(.9385);transform-origin:0 0;
    background:var(--paper);overflow:hidden;
    font-family:"Raleway",sans-serif;color:var(--ink);
  }
  .shapes{position:absolute;inset:0;width:895px;height:1265px}
  .brand{position:absolute;right:58px;top:46px;text-align:right}
  .brand-name{font-size:58px;font-weight:600;color:var(--ink);letter-spacing:-1px;line-height:1}
  .brand-name .dot{display:inline-block;width:14px;height:14px;background:var(--orange);margin-left:8px;vertical-align:middle}
  .brand-tag{font-size:17px;font-weight:500;margin-top:14px;color:#222}
  .headline{
    position:absolute;left:580px;top:500px;
    font-family:"Oswald",sans-serif;color:#fff;text-transform:uppercase;
    font-size:50px;line-height:57px;white-space:nowrap;font-weight:400;
  }
  .headline span{display:block}
  .headline .strong{font-weight:600;letter-spacing:-1.5px}
  .headline .light{font-weight:300;letter-spacing:-.5px}
  .intro{position:absolute;left:54px;top:728px;width:800px}
  .intro h1{font-size:27px;font-weight:400;line-height:33px;color:var(--ink)}
  .intro h1 .accent{color:var(--orange);font-weight:700}
  .intro h1 b{font-weight:700}
  .intro p{font-size:15px;line-height:21px;margin-top:7px;color:var(--ink-soft)}
  .services{position:absolute;left:54px;top:884px;display:flex}
  .services ul{list-style:none;width:268px;padding-right:22px}
  .services ul + ul{border-left:1px solid var(--rule);padding-left:13px;margin-left:-13px;width:281px}
  .services li{display:flex;gap:7px;font-size:14.5px;font-weight:700;text-transform:uppercase;line-height:21px;color:var(--ink);margin-bottom:10.5px}
  .services li svg{flex:none;width:18px;height:18px;margin-top:1px}
  .contact{position:absolute;left:54px;top:1110px;color:#fff}
  .social{display:flex;gap:6px;margin-bottom:10px}
  .social span{width:44px;height:44px;border:2px solid #fff;border-radius:50%}
  .contact .line{display:flex;align-items:center;gap:10px;font-size:19px;line-height:29px}
  .contact .line svg{width:16px;height:16px}
  .contact .web b{font-weight:700}
  .contact .mail{font-weight:700}
  .phone{position:absolute;right:55px;top:1182px;display:flex;align-items:center;gap:8px;color:#fff;font-size:32px;font-weight:700}
  .phone svg{width:26px;height:26px}
</style>
</head>
<body>
<div class="canvas">
  <article class="flyer">
    <svg width="0" height="0" style="position:absolute">
      <symbol id="tick" viewBox="0 0 18 18">
        <circle cx="8.5" cy="9.5" r="7" fill="none" stroke="#f15a29" stroke-width="2"/>
        <path d="M5 9l3.2 3.2L16.5 2.5" fill="none" stroke="#f15a29" stroke-width="2.4" stroke-linecap="round"/>
      </symbol>
    </svg>

    <svg class="shapes" viewBox="0 0 895 1265">
      <defs>
        <linearGradient id="photoTone" x1="0" y1="0" x2="1" y2="1">
          <stop offset="0" stop-color="#dfe7ec"/>
          <stop offset=".5" stop-color="#b9c3cb"/>
          <stop offset="1" stop-color="#8e99a5"/>
        </linearGradient>
      </defs>
      <path role="img" aria-label="Photo: three smiling colleagues at an office table, two shaking hands over printed charts"
            d="M0 165H895V690Q600 700 420 705Q250 710 0 660Z" fill="url(#photoTone)"/>
      <path d="M0 660Q250 715 420 708Q620 700 895 680V1265H0Z" fill="var(--paper)"/>
      <path d="M395 712C500 610 640 450 810 447Q860 446 895 462V690Q840 710 690 712Q520 716 395 712Z" fill="var(--orange)"/>
      <path d="M0 1092Q230 1080 420 1140Q560 1200 667 1265H0Z" fill="var(--orange)"/>
      <path d="M482 1182Q620 1140 790 1142Q860 1143 895 1155V1265H667Q590 1220 482 1182Z" fill="var(--slate)"/>
    </svg>

    <header class="brand">
      <div class="brand-name">staffsense<span class="dot"></span></div>
      <div class="brand-tag">Intelligent Employment Advice</div>
    </header>

    <h2 class="headline">
      <span class="strong">$5 Squabble</span>
      <span class="light">Turns to</span>
      <span class="strong">$12K Payout</span>
    </h2>

    <section class="intro">
      <h1>Introducing <span class="accent">StaffSense</span> the <b>smart choice for Employers</b> needing Intelligent Employment Advice.</h1>
      <p>We will with any Employment problem from checking that your employment contracts are current through to dealing with disputes and grieavances. We offer direct and helpful advice. We are cost effective and understand the needs of business. We are about solving problems, not protracting them.</p>
    </section>

    <section class="services">
      <ul>
        <li><svg><use href="#tick"/></svg>Personal grievances raised against you by an employee</li>
        <li><svg><use href="#tick"/></svg>Independent employment investigations</li>
        <li><svg><use href="#tick"/></svg>Investigation meetings</li>
        <li><svg><use href="#tick"/></svg>Disciplinary meetings</li>
      </ul>
      <ul>
        <li><svg><use href="#tick"/></svg>Misconduct and serious misconduct</li>
        <li><svg><use href="#tick"/></svg>Employee dismissals</li>
        <li><svg><use href="#tick"/></svg>Abuse of sick leave</li>
        <li><svg><use href="#tick"/></svg>Restructuring and redundancies</li>
        <li><svg><use href="#tick"/></svg>Employment contracts drafting and checking</li>
      </ul>
      <ul>
        <li><svg><use href="#tick"/></svg>Poor performers</li>
        <li><svg><use href="#tick"/></svg>90 day trials</li>
        <li><svg><use href="#tick"/></svg>Workplace drug testing advice</li>
        <li><svg><use href="#tick"/></svg>Parental leave</li>
        <li><svg><use href="#tick"/></svg>Exit management</li>
        <li><svg><use href="#tick"/></svg>Medical incapacity</li>
      </ul>
    </section>

    <footer>
      <div class="contact">
        <div class="social"><span></span><span></span></div>
        <div class="line web">
          <svg viewBox="0 0 16 16"><circle cx="8" cy="8" r="6.5" fill="none" stroke="#fff" stroke-width="1.4"/><path d="M7 5l4 4-2 .4 1 2.3-1 .4-1-2.3L7 11z" fill="#fff"/></svg>
          <span>www.<b>staffsense</b>.co.nz</span>
        </div>
        <div class="line mail">
          <svg viewBox="0 0 16 16"><circle cx="8" cy="8" r="6.5" fill="none" stroke="#fff" stroke-width="1.4"/><rect x="4.5" y="5.5" width="7" height="5" fill="none" stroke="#fff" stroke-width="1.1"/><path d="M4.5 5.5L8 8.5l3.5-3" fill="none" stroke="#fff" stroke-width="1.1"/></svg>
          <span>support@staffsense.co.nz</span>
        </div>
      </div>
      <div class="phone">
        <svg viewBox="0 0 26 26"><circle cx="13" cy="13" r="11.5" fill="none" stroke="#fff" stroke-width="1.6"/><path d="M9.5 7.5l2 .2.8 3-1.4 1.1c.7 1.5 1.8 2.6 3.3 3.3l1.1-1.4 3 .8.2 2c-.4.8-1.5 1.2-2.4 1-4.3-.8-7.5-4-8.3-8.3-.2-.9.2-2 1-2.4z" fill="#fff"/></svg>
        <span>0800 55 41 07</span>
      </div>
    </footer>
  </article>
</div>
</body>
</html>
```